Dental Business Card Design w/logo

Classic, elegant w/a touch of contemporary
Upscale dental facility located in Modesto CA
Specializing in restorative & general dentistry
Providing exceptional customer service to the community
Updates

I prefer script and not bold writing
If you can use the phone; fax and email icons instead of spelling them out, it would be great
No bold colors
Classy and elegant
In the back of the card I would like to see something like this
Your Next Appointment:
Mon     Tue    Wed    Thur (a box next to each of them for marking)
Date:_______________ at_____________ AM    PM  (a box next to them for marking)

Thank you

Target Market(s)

Well established professional

Industry/Entity Type

Dental

Contact Information for Business Card

Lavinteya Morbundi DMD
4176 Larkspur Rd
Suite F7
Brellham, CA 95418

Office: 209-731-5902
Fax: 209-731-8417
Email: morbundidmd@velmoranet.com

Requirements
Must have
• Unique classic logo
An easily repeatable design that can be used on letterhead and envelopes
Nice to have
• My initials incorporated into unique design
Should not have
• No cartoons or cheesy themes. This is a practice for the well established and professional individual.

```html
<!DOCTYPE html>
<html lang="en">
<head>
<meta charset="utf-8">
<title>Lavinteya Morbundi DMD – Business Card</title>
<link href="https://fonts.googleapis.com/css2?family=Open+Sans:wght@400;600;700&display=swap" rel="stylesheet">
<style>
  :root {
    --canvas-bg: #e6e6e4;
    --card-bg: #f7f7f5;
    --ink: #1f1f1f;
    --ink-soft: #3a3a3a;
    --accent: #1c6e8c;
    --rule: #4a4a4a;
  }
  * { box-sizing: border-box; margin: 0; padding: 0; }
  html, body {
    width: 1200px;
    height: 756px;
    overflow: hidden;
    background: var(--canvas-bg);
    font-family: "Open Sans", Arial, sans-serif;
  }
  .business-card {
    position: absolute;
    left: 75px;
    top: 78px;
    width: 1050px;
    height: 600px;
    background: var(--card-bg);
    box-shadow: 0 6px 24px rgba(0,0,0,0.12);
    overflow: hidden;
  }
  .name-block {
    position: absolute;
    left: 340px;
    top: 112px;
    width: 640px;
  }
  .doctor-name {
    font-size: 54px;
    font-weight: 400;
    color: var(--ink);
    letter-spacing: 0.5px;
    line-height: 1;
    white-space: nowrap;
  }
  .doctor-name .surname { color: var(--accent); }
  .title-rule {
    display: flex;
    align-items: center;
    margin-top: 14px;
  }
  .title-rule .line {
    flex: 1;
    height: 1.5px;
    background: var(--rule);
  }
  .title-rule .degree {
    font-size: 28px;
    color: var(--ink-soft);
    margin: 0 6px;
    line-height: 1;
    position: relative;
    top: -12px;
  }
  .title-rule .tail {
    width: 14px;
    height: 1.5px;
    background: var(--rule);
    position: relative;
    top: -12px;
  }
  .practice-mark {
    position: absolute;
    left: 70px;
    top: 262px;
    display: flex;
    align-items: center;
    gap: 14px;
  }
  .practice-mark .dot {
    width: 22px;
    height: 22px;
    border-radius: 50%;
    background: var(--accent);
  }
  .practice-mark .practice-name {
    font-size: 30px;
    font-weight: 400;
    color: var(--ink);
  }
  .contact-list {
    position: absolute;
    left: 70px;
    top: 400px;
    font-size: 24px;
    color: var(--ink-soft);
    line-height: 40px;
    list-style: none;
    white-space: nowrap;
  }
  .contact-list .label {
    font-weight: 700;
    color: var(--ink);
  }
  .contact-list .gap { margin-left: 14px; }
  .accent-band {
    position: absolute;
    left: 0;
    bottom: 0;
    width: 100%;
    height: 34px;
    background: var(--accent);
  }
</style>
</head>
<body>
  <article class="business-card">
    <header class="name-block">
      <h1 class="doctor-name">Lavinteya <span class="surname">Morbundi</span></h1>
      <div class="title-rule">
        <span class="line"></span>
        <span class="degree">DMD</span>
        <span class="tail"></span>
      </div>
    </header>

    <div class="practice-mark">
      <span class="dot"></span>
      <span class="practice-name">Morbundi Dental</span>
    </div>

    <ul class="contact-list">
      <li><span class="label">Office:</span> 209-731-5902 <span class="label gap">Fax:</span> 209-731-8417</li>
      <li><span class="label">Address:</span> 4176 Larkspur Rd Suite F7 Brellham, CA 95418</li>
      <li><span class="label">Email:</span> morbundidmd@velmoranet.com</li>
    </ul>

    <div class="accent-band"></div>
  </article>
</body>
</html>
```